KRV Business Cards

We are a local commercial development company based in Silicon Valley and we would like a new business card. I've attached a copy of our company brochure to give a flavor of what we do, our logo, info company colors/graphics, and our current business card. We don't necessarily need a crazy makeover, but would like something that feels a little bit more "fresh" and modern (we've had the same business card design for 15+ years), but still in keeping with our overall brand -- clean, high-quality, modern but timeless. Would like to add our website to the info on the card (www.lumbrel.com) and would like the flexibility for some folks to have an efax number listed and some not to have that included (without it looking like there is a hole).

```html
<!DOCTYPE html>
<html lang="en">
<head>
<meta charset="utf-8">
<title>KRV Business Cards</title>
<link href="https://fonts.googleapis.com/css2?family=Cinzel:wght@400;700&family=Crimson+Text:ital@1&family=Roboto:wght@400&display=swap" rel="stylesheet">
<style>
  :root {
    --bg: #161616;
    --card-dark: #2e4c66;
    --card-light: #4d6f89;
    --ink: #ffffff;
    --accent: #7fb2e6;
    --rule: rgba(140, 185, 230, 0.55);
  }
  * { margin: 0; padding: 0; box-sizing: border-box; }
  html, body { width: 1200px; height: 1200px; overflow: hidden; background: var(--bg); }
  .stage { position: relative; width: 1200px; height: 1200px; }
  .card {
    position: absolute; left: 160px; width: 880px; height: 503px;
    background: linear-gradient(135deg, var(--card-dark) 0%, #3a5b76 55%, var(--card-light) 100%);
    color: var(--ink);
  }
  .card--front { top: 72px; }
  .card--back { top: 625px; }
  .brand {
    position: absolute; display: flex; align-items: center; gap: 14px;
    font-family: "Roboto", sans-serif; font-weight: 400; color: var(--ink);
    white-space: nowrap;
  }
  .brand__square { width: 16px; height: 16px; background: var(--ink); flex: none; }
  .card--front .brand { left: 0; right: 0; top: 215px; justify-content: center; font-size: 30px; }
  .front-url {
    position: absolute; left: 0; right: 0; top: 405px; text-align: center;
    font-family: "Roboto", sans-serif; font-size: 15px; letter-spacing: 9px;
  }
  .card--back .brand { left: 70px; width: 360px; top: 180px; justify-content: center; font-size: 22px; gap: 10px; }
  .card--back .brand__square { width: 12px; height: 12px; }
  .tagline {
    position: absolute; left: 70px; width: 360px; top: 240px; text-align: center;
    font-family: "Crimson Text", serif; font-style: italic; font-size: 23px; line-height: 1.15;
  }
  .contact { position: absolute; left: 488px; top: 100px; width: 345px; font-family: "Roboto", sans-serif; }
  .contact__name { font-family: "Cinzel", serif; font-weight: 700; font-size: 31px; letter-spacing: 1px; line-height: 1; white-space: nowrap; }
  .contact__title { font-family: "Cinzel", serif; font-size: 20px; letter-spacing: 2px; margin-top: 4px; }
  .row { display: flex; align-items: center; gap: 12px; font-size: 20px; height: 36px; }
  .row svg { width: 20px; height: 20px; flex: none; fill: var(--accent); }
  .row--mobile { color: var(--accent); font-size: 23px; height: 42px; }
  .rule { border-top: 1px solid var(--rule); margin: 4px 0 6px; }
  .row--address { align-items: flex-start; height: auto; line-height: 1.3; margin-top: 8px; }
</style>
</head>
<body>
<main class="stage">
  <section class="card card--front">
    <div class="brand"><span class="brand__square"></span>KRV Development Company, LLC</div>
    <div class="front-url">WWW.LUMBREL.COM</div>
  </section>

  <section class="card card--back">
    <div class="brand"><span class="brand__square"></span>KRV Development Company, LLC</div>
    <p class="tagline">Excellence in<br>Commercial Development</p>

    <div class="contact">
      <h1 class="contact__name">Elena M. Hart</h1>
      <p class="contact__title">PARTNER</p>
      <div class="row row--mobile">
        <svg viewBox="0 0 20 20"><path d="M5 1h10a1 1 0 0 1 1 1v16a1 1 0 0 1-1 1H5a1 1 0 0 1-1-1V2a1 1 0 0 1 1-1zm1 2v11h8V3zm4 12.5a1 1 0 1 0 0 2 1 1 0 0 0 0-2z"/></svg>
        650.555.0142
      </div>
      <div class="rule"></div>
      <div class="row">
        <svg viewBox="0 0 20 20"><path d="M4 2l3 0 2 5-2 1.5c1 2.2 2.3 3.5 4.5 4.5L13 11l5 2v3a2 2 0 0 1-2 2C8.5 18 2 11.5 2 4a2 2 0 0 1 2-2z"/></svg>
        650.555.0190
      </div>
      <div class="row">
        <svg viewBox="0 0 20 20"><path d="M5 2h10v4H5zM3 7h14a1 1 0 0 1 1 1v6h-3v4H5v-4H2V8a1 1 0 0 1 1-1zm4 6v3h6v-3z"/></svg>
        650.555.0173
      </div>
      <div class="rule"></div>
      <div class="row">
        <svg viewBox="0 0 20 20"><path d="M2 4h16v12H2zm1.5 1.5v.4L10 11l6.5-5.1v-.4zm0 2.3v6.7h13V7.8L10 12.9z"/></svg>
        elena@lumbrel.com
      </div>
      <div class="rule"></div>
      <div class="row">
        <svg viewBox="0 0 20 20"><path d="M10 1.5a8.5 8.5 0 1 0 0 17 8.5 8.5 0 0 0 0-17zm0 1.5c.9 0 2 1.9 2.4 5H7.6C8 4.9 9.1 3 10 3zM6.1 8H3.3a7 7 0 0 1 4-4.5C6.7 4.7 6.3 6.2 6.1 8zm7.8 0c-.2-1.8-.6-3.3-1.2-4.5a7 7 0 0 1 4 4.5zM3.1 9.5h3V10.5h-3zm4.4 0h5v1h-5zm6.4 0h3v1h-3zM3.3 12h2.8c.2 1.8.6 3.3 1.2 4.5a7 7 0 0 1-4-4.5zm4.3 0h4.8c-.4 3.1-1.5 5-2.4 5s-2-1.9-2.4-5zm6.3 0h2.8a7 7 0 0 1-4 4.5c.6-1.2 1-2.7 1.2-4.5z"/></svg>
        www.lumbrel.com
      </div>
      <div class="rule"></div>
      <div class="row row--address">
        <svg viewBox="0 0 20 20"><path d="M10 1a6 6 0 0 1 6 6c0 4.5-6 12-6 12S4 11.5 4 7a6 6 0 0 1 6-6zm0 3.5a2.5 2.5 0 1 0 0 5 2.5 2.5 0 0 0 0-5z"/></svg>
        <span>218 Larkspur Avenue<br>Larkmont, California 95012</span>
      </div>
    </div>
  </section>
</main>
</body>
</html>
```